Orthodontic Office Needs New Stationary

We have recently renovated our office and are opening a second location. We need new stationary/branding to go with our new look. We like our logo, but are open to changing the colors to match the office look/feel more.

```html
<!DOCTYPE html>
<html lang="en">
<head>
<meta charset="utf-8">
<title>Harlow &amp; Venn Orthodontics – Stationery</title>
<link href="https://fonts.googleapis.com/css2?family=Open+Sans:wght@400;600&family=Roboto:wght@400;500;700&display=swap" rel="stylesheet">
<style>
:root{
  --bg:#e7e7e7;
  --paper:#eeeeee;
  --paper-edge:#f4f4f4;
  --brand:#2d5f7c;
  --ink:#3c3c3c;
  --muted:#5a5a5a;
  --line:#d6d6d6;
}
*{margin:0;padding:0;box-sizing:border-box}
html,body{width:1200px;height:795px;overflow:hidden;background:var(--bg)}
.canvas{position:relative;width:1200px;height:795px;background:var(--bg);font-family:"Open Sans",sans-serif;color:var(--ink)}
.sheet{position:absolute;background:var(--paper);box-shadow:0 2px 6px rgba(0,0,0,.12)}

.wordmark{font-family:"Open Sans",sans-serif;font-weight:400;color:var(--brand);text-align:center;line-height:1.05;white-space:nowrap}
.wordmark .sub{display:block;letter-spacing:.42em}

.letterhead{left:292px;top:99px;width:293px;height:415px}
.letterhead .wordmark{position:absolute;left:0;right:0;top:23px;font-size:12px}
.letterhead .wordmark .sub{font-size:6.4px;letter-spacing:.5em}
.letter-body{position:absolute;left:26px;width:241px;top:102px;font-size:5.3px;line-height:8px;color:var(--ink)}
.letter-body p{text-align:justify;margin-bottom:8px}
.signature{width:36px;height:32px;background:#e3e3e3;border-radius:3px;margin-top:4px}
.letter-footer{position:absolute;left:0;right:0;top:372px;text-align:center;font-family:"Roboto",sans-serif;font-size:4.7px;line-height:7.5px;color:var(--muted)}
.letter-footer .firm{color:var(--brand);font-weight:500}
.letter-footer svg{width:5px;height:5px;vertical-align:-1px;fill:var(--brand)}

.folder{left:636px;top:80px;width:347px;height:437px}
.folder .spine{position:absolute;top:0;bottom:0;width:1px;background:var(--line)}
.folder .wordmark{position:absolute;left:20px;right:0;top:196px;font-size:25px}
.folder .wordmark .sub{font-size:15px;letter-spacing:.52em;margin-left:.5em}

.card{position:absolute;left:187px;width:132px;height:75px;box-shadow:0 2px 5px rgba(0,0,0,.14)}
.card-front{top:551px;background:var(--paper)}
.card-front .mark{position:absolute;left:10px;top:22px;width:56px;text-align:center}
.card-front .circle{width:18px;height:18px;border:1px solid var(--brand);border-radius:50%;margin:0 auto 3px}
.card-front .wordmark{font-size:6px}
.card-front .wordmark .sub{font-size:3.4px;letter-spacing:.3em}
.card-front .divider{position:absolute;left:71px;top:19px;width:1px;height:38px;background:var(--brand)}
.card-front .details{position:absolute;left:76px;top:20px;font-family:"Roboto",sans-serif;font-size:3px;line-height:3.8px;color:var(--muted)}
.card-front .name{font-size:4.2px;font-weight:700;color:var(--brand);line-height:4.4px}
.card-front .firm{color:var(--brand);font-weight:500;margin-top:3px}
.card-back{top:646px;background:var(--brand)}
.card-back .mark{position:absolute;left:0;right:0;top:15px;text-align:center}
.card-back .circle{width:28px;height:28px;border:1.2px solid #f1f1f1;border-radius:50%;margin:0 auto 4px}
.card-back .wordmark{color:#f1f1f1;font-size:9px}
.card-back .wordmark .sub{font-size:5px;letter-spacing:.42em}

.envelope{top:561px;width:329px;height:157px}
.envelope-front{left:353px}
.envelope-front .wordmark{position:absolute;left:22px;top:22px;font-size:10.5px;text-align:left}
.envelope-front .wordmark .sub{font-size:6px;letter-spacing:.48em}
.envelope-back{left:714px}
.envelope-back svg.flap{position:absolute;left:0;top:0;width:329px;height:60px}
.envelope-back .return{position:absolute;left:0;right:0;top:19px;text-align:center;font-family:"Roboto",sans-serif;font-size:5.8px;line-height:8px;color:var(--muted)}
.envelope-back .return .firm{color:var(--brand);font-weight:500;font-size:6.4px}
</style>
</head>
<body>
<main class="canvas">

  <section class="sheet letterhead">
    <div class="wordmark">HARLOW &amp; VENN<span class="sub">ORTHODONTICS</span></div>
    <div class="letter-body">
      <p>Dear customer,</p>
      <p>Lorem ipsum dolor sit amet, consectetur adipisicing elit, sed do eiusmod tempor incididunt ut labore et dolore magna aliqua. Ut enim ad minim veniam, quis nostrud exercitation ullamco laboris nisi ut aliquip ex ea commodo consequat. Duis aute irure dolor in reprehenderit in voluptate velit esse cillum dolore eu fugiat nulla pariatur. Excepteur sint occaecat cupidatat non proident, sunt in culpa qui officia deserunt mollit anim id est laborum.</p>
      <p>Lorem ipsum dolor sit amet, consectetur adipisicing elit, sed do eiusmod tempor incididunt ut labore et dolore magna aliqua. Ut enim ad minim veniam, quis nostrud exercitation ullamco laboris nisi ut aliquip ex ea commodo consequat. Duis aute irure dolor in reprehenderit in voluptate velit esse cillum dolore eu fugiat nulla pariatur. Excepteur sint occaecat cupidatat non proident, sunt in culpa qui officia deserunt mollit anim id est laborum.</p>
      <p>Lorem ipsum dolor sit amet, consectetur adipisicing elit, sed do eiusmod tempor incididunt ut labore et dolore magna aliqua. Ut enim ad minim veniam, quis nostrud exercitation ullamco laboris nisi ut aliquip ex ea commodo consequat. Duis aute irure dolor in reprehenderit in voluptate velit esse cillum dolore eu fugiat nulla pariatur. Excepteur sint occaecat cupidatat non proident, sunt in culpa qui officia deserunt mollit anim id est laborum.</p>
      <p>Lorem ipsum dolor sit amet, consectetur adipisicing elit, sed do eiusmod tempor incididunt ut labore et dolore magna aliqua. Ut enim ad minim veniam, quis nostrud exercitation ullamco laboris nisi ut aliquip ex ea commodo consequat. Duis aute irure dolor in reprehenderit.</p>
      <p>Yours Sincerely,</p>
      <div class="signature" role="img" aria-label="Handwritten signature"></div>
    </div>
    <footer class="letter-footer">
      <div class="firm">Harlow &amp; Venn Orthodontic</div>
      <div>418 Birchmont Ave. Suite 120 Lakeview, GA 30110 &nbsp;|&nbsp; 960 Cedar Hollow Rd. Suite 300 Fairbrook, GA 30140</div>
      <div>
        <svg viewBox="0 0 10 10"><path d="M2 1l2 0 1 2.5-1.3 1a6 6 0 0 0 2.8 2.8l1-1.3L10 7v2c-5 .5-9-3.5-8-8z"/></svg> +15550142290
        &nbsp;<svg viewBox="0 0 10 10"><path d="M0 2h10v6H0z"/></svg> info@HarlowVennOrtho.com
        &nbsp;<svg viewBox="0 0 10 10"><circle cx="5" cy="5" r="4.3" fill="none" stroke="#2d5f7c" stroke-width="1.2"/></svg> www.HarlowVennOrtho.com
      </div>
    </footer>
  </section>

  <section class="sheet folder">
    <span class="spine" style="left:6px"></span>
    <span class="spine" style="left:11px"></span>
    <span class="spine" style="left:19px"></span>
    <div class="wordmark">HARLOW &amp; VENN<span class="sub">ORTHODONTICS</span></div>
  </section>

  <section class="card card-front">
    <div class="mark">
      <div class="circle"></div>
      <div class="wordmark">HARLOW &amp; VENN<span class="sub">ORTHODONTICS</span></div>
    </div>
    <span class="divider"></span>
    <div class="details">
      <div class="name">DANA WHITFIELD</div>
      <div>Managing Director</div>
      <div class="firm">Harlow &amp; Venn Orthodontic</div>
      <div>75 Maple Crest Lane,</div>
      <div>Ridgefield, ON L2B 4K7</div>
      <div>+15550142290</div>
      <div>info@harlowvenn.com</div>
      <div>www.harlowvenn.com</div>
    </div>
  </section>

  <section class="card card-back">
    <div class="mark">
      <div class="circle"></div>
      <div class="wordmark">HARLOW &amp; VENN<span class="sub">ORTHODONTICS</span></div>
    </div>
  </section>

  <section class="sheet envelope envelope-front">
    <div class="wordmark">HARLOW &amp; VENN<span class="sub">ORTHODONTICS</span></div>
  </section>

  <section class="sheet envelope envelope-back">
    <svg class="flap" viewBox="0 0 329 60" aria-hidden="true">
      <path d="M1 1 L8 52 Q9 56 14 56 L315 56 Q320 56 321 52 L328 1" fill="none" stroke="#d8d8d8" stroke-width="0.8"/>
    </svg>
    <div class="return">
      <div class="firm">Harlow &amp; Venn Orthodontic</div>
      <div>418 Birchmont Ave. Suite 120 Lakeview, GA 30110 &nbsp;|&nbsp; 960 Cedar Hollow Rd. Suite 300 Fairbrook, GA 30140</div>
    </div>
  </section>

</main>
</body>
</html>
```